Internal Web Pages for Metricsy Hub

I need internal web pages (Why Metricsy Hub?, What We Offer, Blog, Testimonials) that match the design of the homepage. These do not need to be as long or in-depth as the landing page (provided for reference) but I will need three, maybe four, total pages (I'll select the max number of pages for now, but these will all be simple and short pages). Also attached is our new logo design for the company.

They are to essentially be:
Why Metricsy Hub? - An About Us and Why Choose Us page rolled into one.
What We Offer - A Services type page
Blog - self-explanatory
Testimonials - Customer Reviews and Use Cases

Also, maybe a very simple "Contact Us" page as well.

Target Market(s)

Business professionals that work with data analytics teams

Industry/Entity Type

Data Science

Number of Pages Required

5+ page

Requirements
Must have
• It must match the original design in theme and colors.
Nice to have
• Simple pages that show continuity that flows from the original landing page.
Should not have
• Can not be a different design that does not match the landing page.

```html
<!DOCTYPE html>
<html lang="en">
<head>
<meta charset="utf-8">
<title>Why Metricsy Hub?</title>
<link href="https://fonts.googleapis.com/css2?family=Poppins:wght@300;400;500;600;700&family=Arimo:wght@400;700&display=swap" rel="stylesheet">
<style>
:root{
  --navy:#1c0b4f;
  --navy-deep:#170842;
  --indigo:#4a50e0;
  --blue:#2673e8;
  --orange:#f5870a;
  --ink:#2b2b33;
  --white:#ffffff;
}
*{box-sizing:border-box;margin:0;padding:0}
html,body{width:1200px;height:3997px;overflow:hidden}
body{position:relative;background:var(--white);font-family:"Arimo",Arial,sans-serif;color:var(--ink)}
.abs{position:absolute}
.heading{font-family:"Poppins",Arial,sans-serif;font-weight:300}

/* header */
.site-header{left:0;top:0;width:1200px;height:86px;background:var(--white)}
.brand{left:93px;top:18px;display:flex;align-items:center;gap:10px;font-family:"Poppins",sans-serif;font-weight:300;font-size:40px;color:var(--indigo)}
.brand-square{width:26px;height:26px;background:var(--indigo)}
.main-nav{left:467px;top:30px;display:flex;gap:32px;font-family:"Poppins",sans-serif;font-size:18px;color:#555}
.main-nav .active{color:var(--indigo)}
.btn{background:var(--orange);color:#fff;font-family:"Poppins",sans-serif;font-weight:600;letter-spacing:.5px;display:flex;align-items:center;justify-content:center;border-radius:3px}
.header-cta{left:975px;top:23px;width:132px;height:39px;font-size:13px}

/* hero */
.hero-title{left:138px;top:172px;color:#fff;font-size:56px;line-height:66px}
.dashboard-shot{background:linear-gradient(90deg,#ffffff 0%,#f7f7fc 32%,#ffffff 34%,#f3f4fb 70%,#ecedf9 100%)}
.hero-shot{left:411px;top:122px;width:800px;height:400px;border-radius:18px 0 0 0}

/* about */
.section-title{font-size:44px;color:var(--ink)}
.rule{height:2px;background:var(--indigo)}
.copy-sm{font-size:14px;line-height:23.3px;color:#333}
.copy-lg{font-size:19px;line-height:23.3px;color:#333}
.browser{left:490px;top:618px;width:597px;height:404px;box-shadow:0 22px 40px rgba(20,20,60,.28);background:#fff}
.browser-bar{height:32px;background:#f5f5fa;display:flex;align-items:center;gap:7px;padding-left:12px}
.browser-bar span{width:6px;height:6px;border-radius:50%;background:#9fa6e8}
.photo-office{height:372px;background:linear-gradient(135deg,#3a4e63 0%,#8a8f94 40%,#d9d2c8 65%,#5b6775 100%)}
.accent-circle{border-radius:50%;background:var(--blue)}

/* feature */
.feature-photo{left:93px;top:1500px;width:469px;height:470px;background:linear-gradient(140deg,#9fb3c4 0%,#d6dde3 45%,#7d94ab 75%,#c8ced4 100%);box-shadow:0 10px 24px rgba(0,0,0,.12)}
.play{left:298px;top:1705px;width:60px;height:60px;border-radius:50%;background:#fff;display:flex;align-items:center;justify-content:center}
.feature-panel{left:562px;top:1500px;width:299px;height:470px;background:var(--blue);color:#fff;padding:38px 18px 0 39px;overflow:hidden}
.feature-panel h2{font-size:33px;line-height:45px;font-weight:300;letter-spacing:-.3px}
.feature-panel p{font-size:13.5px;line-height:23.3px;margin-top:14px;padding-left:2px;padding-right:10px}
.tile-brand{left:885px;top:1500px;width:221px;height:221px;background:#eef0fb;display:flex;align-items:center;justify-content:center;gap:8px;font-family:"Poppins",sans-serif;font-size:17px;color:var(--indigo)}
.tile-brand i{width:14px;height:14px;background:var(--indigo)}
.tile-photo{left:885px;top:1751px;width:221px;height:221px;background:linear-gradient(135deg,#2b2320 0%,#6b4b33 45%,#c79a6a 60%,#3a3a48 100%)}

/* why choose */
.choose-shot{left:110px;top:2128px;width:598px;height:404px;box-shadow:0 16px 34px rgba(20,20,60,.22)}

/* quote */
.quote-title{left:140px;top:3158px;color:#fff;font-size:40px}
.quote-sub{left:143px;top:3228px;color:#fff;font-size:17px;line-height:26px;font-family:"Poppins",sans-serif;font-weight:300}
.quote-cta{left:143px;top:3320px;width:243px;height:52px;font-size:14px;gap:8px;border-radius:0}

/* footer */
.site-footer{left:0;top:3466px;width:1200px;height:396px;background:var(--navy)}
.footer-bottom{left:0;top:3862px;width:1200px;height:135px;background:var(--navy-deep);color:#fff;font-family:"Poppins",sans-serif;font-weight:500;font-size:14px;text-align:center;padding-top:60px}
.footer-brand{left:143px;top:3522px;display:flex;align-items:center;gap:12px;font-family:"Poppins",sans-serif;font-weight:300;font-size:34px;color:#fff}
.footer-brand i{width:28px;height:28px;background:var(--blue)}
.footer-text{color:#e6e4f2;font-family:"Poppins",sans-serif;font-weight:300;font-size:14px;line-height:22.5px}
.social{left:143px;top:3737px;display:flex;gap:7px}
.social span{width:34px;height:34px;border-radius:50%;border:1.5px solid #fff}
.footer-head{color:#fff;font-family:"Poppins",sans-serif;font-weight:600;font-size:18px}
.contact-item{left:480px;display:flex;gap:18px;color:#fff;font-family:"Poppins",sans-serif;font-weight:500;font-size:15px;line-height:21px}
.contact-item svg{flex:none;margin-top:2px}
.email-input{left:754px;top:3675px;width:303px;height:37px;background:#fff;border-radius:3px;font-family:"Poppins",sans-serif;font-size:13px;color:#666;padding:9px 14px}
.subscribe{left:754px;top:3707px;width:126px;height:39px;font-size:13px;border-radius:0}
</style>
</head>
<body>

<header class="abs site-header">
  <div class="abs brand"><span class="brand-square"></span>Metricsy Hub</div>
  <nav class="abs main-nav">
    <span class="active">Home</span><span>About us</span><span>Our Service</span><span>Blog</span><span>Contact</span>
  </nav>
  <div class="abs btn header-cta">GET STARTED</div>
</header>

<svg class="abs" style="left:0;top:0" width="1200" height="560" viewBox="0 0 1200 560">
  <polygon points="0,86 1200,86 1200,419 416,500 0,400" fill="#1c0b4f"/>
  <circle cx="380" cy="155" r="17" fill="#2a1a63"/>
  <circle cx="380" cy="270" r="17" fill="#2a1a63"/>
  <circle cx="380" cy="413" r="17" fill="#2a1a63"/>
</svg>
<h1 class="abs heading hero-title">WHY<br>Metricsy<br>Hub?</h1>

<div class="abs dashboard-shot hero-shot" role="img" aria-label="Screenshot of the analytics dashboard showing a user profile, monthly statistics and saved cards"></div>

<svg class="abs" style="left:0;top:0" width="1200" height="560" viewBox="0 0 1200 560">
  <polygon points="0,400 416,500 1200,419 1200,425 416,512 0,404" fill="#4a50e0"/>
  <polygon points="0,404 416,512 1200,425 1200,560 0,560" fill="#ffffff"/>
</svg>

<h2 class="abs heading section-title" style="left:90px;top:656px">About Us</h2>
<div class="abs rule" style="left:90px;top:730px;width:143px"></div>
<p class="abs copy-sm" style="left:92px;top:758px;width:335px">&nbsp;Lorem Ipsum. Proin gravida nibh vel velit auctor aliquet. Aenean sollicitudin, lorem quis bibendum auctor, nisi elit consequat ipsum, nec sagittis sem nibh id elit. Duis sed odio sit amet nibh vulputate cursus a sit amet mauris. Morbi accumsan ipsum velit. Nam nec tellus a odio tincidunt auctor a ornare odio. Sed non &nbsp;mauris vitae erat consequat auctor eu in elit.</p>

<div class="abs browser">
  <div class="browser-bar"><span></span><span></span><span></span></div>
  <div class="photo-office" role="img" aria-label="Photo of two colleagues smiling and working together at a computer in a bright office"></div>
</div>
<div class="abs accent-circle" style="left:1045px;top:595px;width:74px;height:74px"></div>

<div class="abs copy-lg" style="left:172px;top:1130px;width:820px">
  <p>&nbsp;Lorem Ipsum. Proin gravida nibh vel velit auctor aliquet. Aenean sollicitudin, lorem quis bibendum auctor, nisi elit consequat ipsum, nec sagittis sem nibh id elit. Duis sed odio sit amet nibh vulputate cursus a sit amet mauris. Morbi accumsan ipsum velit. Nam nec tellus a odio tincidunt auctor a ornare odio. Sed non &nbsp;mauris vitae erat consequat auctor eu in elit. Class aptent taciti sociosqu ad litora torquent per conubia nostra, per inceptos himenaeos.</p>
  <p>&nbsp;Mauris in erat justo. Nullam ac urna eu felis dapibus condimentum sit amet a augue. Sed non neque elit. Sed ut imperdiet nisi. Proin condimentum fermentum nunc. Etiam pharetra, erat sed fermentum feugiat, velit mauris egestas quam, ut aliquam massa nisl quis neque. Suspendisse in orci enim.</p>
</div>

<div class="abs feature-photo" role="img" aria-label="Photo of hands holding a tablet showing bar and pie charts on a desk"></div>
<div class="abs play"><svg width="20" height="22" viewBox="0 0 20 22"><polygon points="3,1 19,11 3,21" fill="#2673e8"/></svg></div>
<div class="abs feature-panel">
  <h2 class="heading">Lorem Ipsum. Proin gravida nibh vel velit auctor aliquet. Aenean</h2>
  <p>Lorem Ipsum. Proin gravida nibh vel velit auctor aliquet. Aenean sollicitudin, lorem quis bibendum auctor, nisi elit consequat ipsum, nec sagittis sem nibh id elit. Duis sed odio sit amet nibh</p>
</div>
<div class="abs tile-brand"><i></i>Metricsy Hub</div>
<div class="abs tile-photo" role="img" aria-label="Photo of hands on a laptop keyboard with glowing data charts"></div>

<div class="abs accent-circle" style="left:84px;top:2110px;width:62px;height:62px;z-index:2"></div>
<div class="abs dashboard-shot choose-shot" role="img" aria-label="Screenshot of the analytics dashboard showing a user profile, monthly statistics and investments"></div>

<h2 class="abs heading section-title" style="left:770px;top:2165px">Why Choose Us</h2>
<div class="abs rule" style="left:770px;top:2247px;width:140px"></div>
<p class="abs copy-sm" style="left:770px;top:2281px;width:340px">&nbsp;Lorem Ipsum. Proin gravida nibh vel velit auctor aliquet. Aenean sollicitudin, lorem quis bibendum auctor, nisi elit consequat ipsum, nec sagittis sem nibh id elit. Duis sed odio sit amet nibh vulputate cursus a sit amet mauris. Morbi accumsan ipsum velit. Nam nec tellus a odio tincidunt auctor a ornare odio. Sed non &nbsp;mauris vitae erat consequat auctor eu in elit.</p>

<div class="abs copy-lg" style="left:172px;top:2620px;width:820px">
  <p>&nbsp;Lorem Ipsum. Proin gravida nibh vel velit auctor aliquet. Aenean sollicitudin, lorem quis bibendum auctor, nisi elit consequat ipsum, nec sagittis sem nibh id elit. Duis sed odio sit amet nibh vulputate cursus a sit amet mauris. Morbi accumsan ipsum velit. Nam nec tellus a odio tincidunt auctor a ornare odio. Sed non &nbsp;mauris vitae erat consequat auctor eu in elit. Class aptent taciti sociosqu ad litora torquent per conubia nostra, per inceptos himenaeos.</p>
  <p>&nbsp;Mauris in erat justo. Nullam ac urna eu felis dapibus condimentum sit amet a augue. Sed non neque elit. Sed ut imperdiet nisi. Proin condimentum fermentum nunc. Etiam pharetra, erat sed fermentum feugiat, velit mauris egestas quam, ut aliquam massa nisl quis neque. Suspendisse in orci enim.</p>
</div>

<svg class="abs" style="left:0;top:2960px" width="1200" height="506" viewBox="0 0 1200 506">
  <defs>
    <linearGradient id="band" x1="0" y1="0" x2="1" y2="0">
      <stop offset="0" stop-color="#2a1468"/><stop offset=".6" stop-color="#3a2d86"/><stop offset="1" stop-color="#2b1a6a"/>
    </linearGradient>
    <linearGradient id="photoTone" x1="0" y1="0" x2="1" y2="0">
      <stop offset="0" stop-color="#5a6fa8" stop-opacity="0"/><stop offset=".35" stop-color="#6d84b8" stop-opacity=".75"/><stop offset="1" stop-color="#3b4880" stop-opacity=".85"/>
    </linearGradient>
  </defs>
  <polygon points="0,132 411,25 1200,100 1200,506 0,506" fill="url(#band)"/>
  <path d="M560,506 L560,110 Q700,40 760,22 L880,12 L1000,90 L1000,506 Z" fill="url(#photoTone)" role="img" aria-label="Photo of a man with glasses reading a tablet"/>
  <polygon points="160,92 411,25 740,52 411,36" fill="#4a50e0"/>
</svg>
<h2 class="abs heading quote-title">Request for quotation</h2>
<p class="abs quote-sub">Sed ut perspiciatis unde omnis iste natus<br>voluptatem accusantium doloremque laudantium</p>
<div class="abs btn quote-cta">GET EARLY ACCESS
  <svg width="14" height="12" viewBox="0 0 14 12" fill="none" stroke="#fff" stroke-width="2"><path d="M1 6h11M7 1l5 5-5 5"/></svg></div>

<footer class="abs site-footer"></footer>
<div class="abs footer-brand"><i></i>Metricsy Hub</div>
<p class="abs footer-text" style="left:143px;top:3594px;width:290px">Sed ut perspiciatis unde omnis iste natus error sit voluptatem accusantium doloremque laudantium, totam rem aperiam, eaque ipsa quae ab illo inventore veritatis et quasi</p>
<div class="abs social"><span></span><span></span><span></span><span></span></div>

<div class="abs footer-head" style="left:480px;top:3527px">CONTACT US</div>
<div class="abs contact-item" style="top:3580px">
  <svg width="18" height="20" viewBox="0 0 18 20" fill="none" stroke="#fff" stroke-width="1.4"><path d="M9 19s6-6 6-11A6 6 0 0 0 3 8c0 5 6 11 6 11z"/><circle cx="9" cy="8" r="2"/></svg>
  <div>Metricsy Hub<br>250 ipsam voluptatem<br>quia voluptas</div>
</div>
<div class="abs contact-item" style="top:3670px">
  <svg width="18" height="18" viewBox="0 0 18 18" fill="none" stroke="#fff" stroke-width="1.4"><path d="M3 2h4l1.5 4-2 1.5a9 9 0 0 0 4 4L12 9.5l4 1.5v4a2 2 0 0 1-2 2A14 14 0 0 1 1 4a2 2 0 0 1 2-2z"/></svg>
  <div>Phone :<br>555-0140-2200</div>
</div>
<div class="abs contact-item" style="top:3734px">
  <svg width="18" height="14" viewBox="0 0 18 14" fill="none" stroke="#fff" stroke-width="1.4"><rect x="1" y="1" width="16" height="12"/><path d="M1 1l8 7 8-7"/></svg>
  <div>Email :<br>info@metricsyhub.example</div>
</div>

<div class="abs footer-head" style="left:754px;top:3527px">SIGN UP TO RECEIVE EMAIL</div>
<p class="abs footer-text" style="left:754px;top:3574px;width:310px;font-size:13px;line-height:24px">Excepteur sint occaecat cupidatat non proident, sunt in culpa qui Nemo enim ipsam vo-</p>
<div class="abs email-input">Enter Email</div>
<div class="abs btn subscribe">SUBSCRIBE</div>

<div class="abs footer-bottom">Copyright © Metricsy Hub 2021. All rights reserved. | Privacy Policy</div>

</body>
</html>
```